Tranquil Pathway Business Card

Logo attached. (will be printing onto thick white/off white textured card)

Double sided business card for two Therapists working at Tranquil Pathway.

Require one design, but with different name and mobile numbers on each card.

Target Market(s)

Medical, Health

Industry/Entity Type

Business

Contact Information for Business Card

Need one business card design, but a separate card for each person - Colin Marchetti and Marieke de Boeckx.

FRONT OF CARD

Logo

Name (Colin Marchetti on one card, Marieke de Boeckx on the other)
Professional Clinical Hypnotherapist

Consulting Rooms (Near Lindqvist Hospital)
482 Brackenfield Road
Dunmore VIC 3987

Colin@TranquilPathway.example.au OR Marieke@TranquilPathway.example.au

Mobile: 0455 872 604 (for Colin) OR
Mobile: 0467 290 518 (for Marieke)

BACK OF CARD

Logo

Website: www.TranquilPathway.example.au

Phone: 1300 958 471

Requirements
Must have
• Text and logo only. No additiional graphics.

```html
<!DOCTYPE html>
<html lang="en">
<head>
<meta charset="utf-8">
<title>Tranquil Pathway Business Cards</title>
<link rel="stylesheet" href="https://fonts.googleapis.com/css2?family=Source+Sans+3:wght@400;600;700&display=swap">
<style>
  :root {
    --navy: #222a5c;
    --navy-deep: #1a2050;
    --ring-grey: #6b6b6b;
    --text-grey: #666666;
    --paper: #ffffff;
    --backdrop: #ececec;
    --font: "Source Sans 3", sans-serif;
  }
  * { margin: 0; padding: 0; box-sizing: border-box; }
  html, body { width: 1200px; height: 1200px; overflow: hidden; }
  body { background: var(--backdrop); font-family: var(--font); position: relative; }

  .card {
    position: absolute; left: 320px; width: 559px; height: 318px;
    background: var(--paper); overflow: hidden;
    box-shadow: 0 3px 10px rgba(0,0,0,0.18);
  }
  .card--colin { top: 51px; }
  .card--marieke { top: 420px; }
  .card--back { top: 792px; background: var(--navy); }

  .person-name {
    position: absolute; left: 34px; top: 58px;
    font-size: 20px; font-weight: 700; color: var(--navy);
  }
  .person-title {
    position: absolute; left: 34px; top: 82px;
    font-size: 13.5px; color: var(--text-grey);
  }
  .contact-band {
    position: absolute; left: 0; top: 110px; width: 100%; height: 102px;
    background: var(--navy);
  }
  .contact-row {
    position: absolute; left: 34px; display: flex; align-items: center; gap: 7px;
    font-size: 14px; color: var(--paper);
  }
  .contact-row--phone { top: 25px; }
  .contact-row--email { top: 51px; }
  .contact-row svg { width: 15px; height: 15px; flex: none; }

  .brand-mark {
    position: absolute; right: 22px; top: 50px; transform: translateY(-50%);
    display: flex; align-items: center; gap: 12px;
  }
  .brand-mark__circle {
    width: 104px; height: 104px; border-radius: 50%; background: var(--ring-grey); flex: none;
  }
  .brand-mark__name {
    font-size: 17px; font-weight: 700; color: var(--paper); line-height: 1.1; text-align: right;
  }

  .address {
    position: absolute; left: 34px; top: 216px;
    font-size: 14px; line-height: 19px; color: var(--text-grey);
  }
  .address strong { font-weight: 700; }

  .back-logo {
    position: absolute; left: 118px; top: 72px; height: 100px;
    display: flex; align-items: center; gap: 14px;
  }
  .back-logo__circle {
    width: 96px; height: 96px; border-radius: 50%; background: var(--ring-grey); flex: none;
  }
  .back-logo__divider { width: 2px; height: 100px; background: var(--ring-grey); }
  .back-logo__name {
    font-size: 30px; font-weight: 700; color: var(--paper); line-height: 1.02; letter-spacing: 0.5px;
  }
  .back-strip {
    position: absolute; left: 0; top: 210px; width: 100%; height: 34px;
    background: var(--navy-deep);
    display: flex; align-items: center; justify-content: center; gap: 8px;
    color: var(--paper); font-size: 14px;
  }
  .back-strip svg { width: 18px; height: 18px; }
  .back-strip__phone { font-weight: 700; font-size: 17px; }
  .back-strip__sep { opacity: 0.7; }
  .back-strip__web strong { font-weight: 600; }

  .caption {
    position: absolute; top: 1131px; left: 0; width: 100%; text-align: center;
    font-size: 19px; color: #333;
  }
</style>
</head>
<body>

<section class="card card--colin">
  <p class="person-name">Colin Marchetti</p>
  <p class="person-title">Professional Clinical Hypnotherapist</p>
  <div class="contact-band">
    <p class="contact-row contact-row--phone">
      <svg viewBox="0 0 16 16"><rect x="1" y="1" width="14" height="14" rx="4" fill="#fff"/><rect x="5" y="3.5" width="6" height="9" rx="1" fill="none" stroke="#222a5c" stroke-width="1.3"/></svg>
      0455 872 604
    </p>
    <p class="contact-row contact-row--email">
      <svg viewBox="0 0 16 16"><circle cx="8" cy="8" r="7.5" fill="#fff"/><rect x="4" y="5" width="8" height="6" fill="none" stroke="#222a5c" stroke-width="1.1"/><path d="M4 5l4 3.2L12 5" fill="none" stroke="#222a5c" stroke-width="1.1"/></svg>
      Colin@TranquilPathway.example.au
    </p>
    <div class="brand-mark">
      <span class="brand-mark__name">Tranquil<br>Pathway</span>
      <span class="brand-mark__circle"></span>
    </div>
  </div>
  <p class="address"><strong>Consulting Rooms</strong> (Near Lindqvist Hospital)<br>482 Brackenfield Road<br>Dunmore VIC 3987</p>
</section>

<section class="card card--marieke">
  <p class="person-name">Marieke de Boeckx</p>
  <p class="person-title">Professional Clinical Hypnotherapist</p>
  <div class="contact-band">
    <p class="contact-row contact-row--phone">
      <svg viewBox="0 0 16 16"><rect x="1" y="1" width="14" height="14" rx="4" fill="#fff"/><rect x="5" y="3.5" width="6" height="9" rx="1" fill="none" stroke="#222a5c" stroke-width="1.3"/></svg>
      0467 290 518
    </p>
    <p class="contact-row contact-row--email">
      <svg viewBox="0 0 16 16"><circle cx="8" cy="8" r="7.5" fill="#fff"/><rect x="4" y="5" width="8" height="6" fill="none" stroke="#222a5c" stroke-width="1.1"/><path d="M4 5l4 3.2L12 5" fill="none" stroke="#222a5c" stroke-width="1.1"/></svg>
      Marieke@TranquilPathway.example.au
    </p>
    <div class="brand-mark">
      <span class="brand-mark__name">Tranquil<br>Pathway</span>
      <span class="brand-mark__circle"></span>
    </div>
  </div>
  <p class="address"><strong>Consulting Rooms</strong> (Near Lindqvist Hospital)<br>482 Brackenfield Road<br>Dunmore VIC 3987</p>
</section>

<section class="card card--back">
  <div class="back-logo">
    <span class="back-logo__circle"></span>
    <span class="back-logo__divider"></span>
    <span class="back-logo__name">TRANQUIL<br>PATHWAY</span>
  </div>
  <div class="back-strip">
    <svg viewBox="0 0 18 18"><circle cx="9" cy="9" r="8.5" fill="#fff"/><path d="M6 4.5c.6-.3 1.1 0 1.4.6l.6 1.4c.2.5 0 .9-.4 1.2l-.5.4c.5 1.1 1.3 1.9 2.4 2.4l.4-.5c.3-.4.7-.6 1.2-.4l1.4.6c.6.3.9.8.6 1.4-.4 1-1.3 1.6-2.3 1.4C7.6 12.4 5.6 10.4 4.9 7.2 4.7 6 5.1 5 6 4.5z" fill="#1a2050"/></svg>
    <span class="back-strip__phone">1300 958 471</span>
    <span class="back-strip__sep">|</span>
    <span class="back-strip__web">www.<strong>TranquilPathway</strong>.example.au</span>
  </div>
</section>

<p class="caption">( Back of Card )</p>

</body>
</html>
```